Energy trading company (Voltarix) needs a business card

We need a business card for a company based in Central America. Our main purpose is trading energy . We already have the logo but we need some good creativity to design a high impact business card. Colors blue, orange, green can be used or we would like to see good combinatios with our logo

Target Market(s)

Energy

Industry/Entity Type

Power Generation

Contact Information for Business Card

Logo , headquarters , name, background

Font styles to use
Serif
Sans Serif

Colors

Designer to choose colors to be used in the design.

Requirements
Must have
• it must have a fresh and clean view
Nice to have
• good backgrounds that combine with the logo
Should not have
• too much words

```html
<!DOCTYPE html>
<html lang="en">
<head>
<meta charset="utf-8">
<title>Voltarix Business Card</title>
<link rel="stylesheet" href="https://fonts.googleapis.com/css2?family=Montserrat:wght@400&family=Oswald:wght@600&family=Arimo:wght@400;700&display=swap">
<style>
  :root {
    --sky-top: #5aaee0;
    --sky-mid: #2f7cc6;
    --sky-deep: #1a54a6;
    --flag-blue: #0a6dbb;
    --signal-orange: #f7941d;
    --signal-green: #22b04b;
    --paper: #ffffff;
  }
  html, body {
    margin: 0;
    padding: 0;
    width: 1200px;
    height: 720px;
    overflow: hidden;
    background: #e9edf2;
  }
  .card {
    position: relative;
    width: 1200px;
    height: 720px;
    overflow: hidden;
    background: linear-gradient(180deg, var(--sky-top) 0%, var(--sky-mid) 45%, var(--sky-deep) 100%);
  }
  .card-art {
    position: absolute;
    inset: 0;
    width: 1200px;
    height: 720px;
  }
  .brand-mark {
    position: absolute;
    left: 310px;
    top: 150px;
    width: 116px;
    height: 116px;
    border-radius: 50%;
    background: var(--paper);
  }
  .brand-name {
    position: absolute;
    left: 142px;
    top: 275px;
    margin: 0;
    font-family: "Montserrat", sans-serif;
    font-weight: 400;
    font-size: 92px;
    line-height: 1;
    letter-spacing: 0;
    color: var(--paper);
  }
  .office-label {
    position: absolute;
    left: 172px;
    top: 465px;
    margin: 0;
    font-family: "Oswald", sans-serif;
    font-weight: 600;
    font-size: 60px;
    line-height: 1;
    letter-spacing: -0.5px;
    color: var(--paper);
  }
  .holder {
    position: absolute;
    left: 644px;
    top: 146px;
    margin: 0;
    font-family: "Arimo", sans-serif;
    color: var(--paper);
  }
  .holder-name {
    display: block;
    font-weight: 700;
    font-size: 44px;
    line-height: 1.2;
  }
  .holder-title {
    display: block;
    font-weight: 400;
    font-size: 33px;
    line-height: 1.3;
    margin-top: 2px;
  }
</style>
</head>
<body>
  <div class="card">
    <svg class="card-art" viewBox="0 0 1125 675">
      <defs>
        <linearGradient id="network-tone" x1="0" y1="0" x2="1" y2="1">
          <stop offset="0" stop-color="#ffffff" stop-opacity="0.10"/>
          <stop offset="1" stop-color="#ffffff" stop-opacity="0.22"/>
        </linearGradient>
      </defs>

      <g class="flag-band">
        <polygon class="flag-stripes-area" role="img" aria-label="Flag stripes artwork" points="0,295 1125,610 1125,675 0,675" fill="var(--signal-orange)"/>
        <polygon class="flag-canton-area" role="img" aria-label="Flag star field artwork" points="0,295 430,415 430,675 0,675" fill="var(--flag-blue)"/>
      </g>

      <rect class="network-area" role="img" aria-label="Energy network circuit illustration" x="610" y="250" width="515" height="425" fill="url(#network-tone)"/>

      <g class="office-tag">
        <polygon points="139,399 556,399 556,454 604,474 556,494 556,549 139,549" fill="var(--paper)"/>
        <polygon points="135,395 552,395 552,450 600,470 552,490 552,545 135,545" fill="var(--signal-green)"/>
      </g>
    </svg>

    <div class="brand-mark"></div>
    <h1 class="brand-name">VOLTARIX</h1>
    <p class="office-label">HEADQUARTERS</p>
    <p class="holder">
      <span class="holder-name">NAME : XXXXXXXX</span>
      <span class="holder-title">TITLE : XXXXXX</span>
    </p>
  </div>
</body>
</html>
```